Poster Design October

We are a Poker Club (Lakeview Veterans Hall Poker Club). We run poker tournaments three night a week in Mount Gambier
We require a poster to advertise our upcoming major Poker tournament
The details of the event are set out below
ANNUAL $200 BUY IN TOURNAMENT
OCTOBER LONG WEEK END
4-5 OCTOBER 2014
$100K STARTING STACK
45 MIN BLINDS
LAKEVIEW VETERANS HALL
42 KERRIDGE LANE
MOUNT GAMBIER SA 5290
10:00AM START (SA TIME)
REGISTRATION 9:30AM (SA TIME)
EMAIL LVHCARDS@MAILNEST.COM.AU FOR MORE INFORMATION
FIND US ON FRIENDBOOK: LVH CARDS 2014
I have attached a flyer this is something like what we are looking for
I Have also attached the LVH logo which need to be included
Target Market(s)
Poker plyers 18+ both genders
Industry/Entity Type
Club

```html
<!DOCTYPE html>
<html lang="en">
<head>
<meta charset="utf-8">
<title>Annual $200 Buy In Tournament – Lakeview Veterans Hall Poker Club</title>
<link rel="stylesheet" href="https://fonts.googleapis.com/css2?family=Anton&family=Open+Sans:wght@600;700;800&display=swap">
<style>
  :root {
    --sky-orange: #f4952a;
    --hot-red: #d5162a;
    --royal-purple: #6c2a8e;
    --night-navy: #1f1a5e;
    --marquee-yellow: #ffe800;
    --title-yellow: #fff200;
    --ink: #111111;
    --paper: #ffffff;
    --burst-top: #f6e3ea;
    --burst-bottom: #c9a3b8;
    --felt: #151515;
    --chip-red: #c8101c;
  }
  html, body {
    margin: 0;
    padding: 0;
    width: 1200px;
    height: 849px;
    overflow: hidden;
  }
  body { font-family: "Open Sans", Arial, sans-serif; }
  .poster {
    position: relative;
    width: 1200px;
    height: 849px;
    overflow: hidden;
    background: linear-gradient(180deg, var(--sky-orange) 0%, var(--hot-red) 30%, var(--royal-purple) 62%, var(--night-navy) 100%);
  }
  .marquee-frame {
    position: absolute;
    inset: 0;
  }
  .club-mark {
    position: absolute;
    left: 1068px;
    top: 36px;
    width: 84px;
    height: 84px;
    background: var(--paper);
    display: flex;
    align-items: center;
    justify-content: center;
    font-weight: 800;
    font-size: 26px;
    color: var(--night-navy);
  }
  .presenter {
    position: absolute;
    left: 0;
    width: 1190px;
    top: 62px;
    text-align: center;
    color: var(--paper);
    font-weight: 700;
    font-size: 29px;
    margin: 0;
  }
  .event-title {
    position: absolute;
    left: 0;
    width: 1190px;
    top: 108px;
    margin: 0;
    text-align: center;
    font-family: "Anton", "Impact", sans-serif;
    font-weight: 400;
    font-size: 66px;
    line-height: 1;
    letter-spacing: 1px;
    color: var(--title-yellow);
    -webkit-text-stroke: 2px var(--ink);
    text-shadow: 4px 4px 0 var(--ink);
  }
  .event-date {
    position: absolute;
    left: 0;
    width: 1190px;
    margin: 0;
    text-align: center;
    color: var(--paper);
    font-weight: 800;
    font-size: 44px;
    line-height: 1;
    text-shadow: 3px 3px 0 var(--ink);
  }
  .event-date.weekend { top: 204px; }
  .event-date.days { top: 262px; }
  .stack-burst {
    position: absolute;
    left: 895px;
    top: 228px;
    width: 200px;
    height: 200px;
  }
  .stack-burst-text {
    position: absolute;
    left: 895px;
    top: 255px;
    width: 200px;
    text-align: center;
    color: var(--ink);
    font-weight: 700;
    font-size: 21px;
    line-height: 26px;
  }
  .stack-burst-text p { margin: 0; }
  .stack-burst-text .blinds { margin-top: 12px; }
  .details {
    position: absolute;
    left: 140px;
    top: 393px;
    color: var(--paper);
    font-weight: 600;
    font-size: 24px;
    line-height: 36.5px;
  }
  .details p { margin: 0; }
  .details .label { color: var(--marquee-yellow); }
  .details .gap { margin-top: 16px; }
  .details .gap-wide { margin-top: 38px; }
  .social {
    position: absolute;
    left: 138px;
    top: 738px;
    display: flex;
    align-items: center;
    gap: 16px;
    color: var(--paper);
    font-weight: 600;
    font-size: 24px;
  }
  .social-tag {
    display: flex;
    align-items: center;
    gap: 8px;
    font-size: 18px;
  }
  .social-tag .dot {
    width: 18px;
    height: 18px;
    background: var(--paper);
  }
  .chips-photo {
    position: absolute;
    left: 600px;
    top: 488px;
    width: 530px;
    height: 320px;
    border-radius: 50% 50% 12px 12px / 40% 40% 12px 12px;
    background:
      radial-gradient(ellipse 40% 45% at 45% 45%, var(--chip-red) 0%, #8e0c14 60%, transparent 75%),
      radial-gradient(ellipse 70% 60% at 55% 70%, #2a2a2a 0%, var(--felt) 70%, transparent 100%);
  }
</style>
</head>
<body>
<main class="poster">
  <svg class="marquee-frame" width="1200" height="849" viewBox="0 0 1200 849" aria-hidden="true">
    <rect x="17" y="17" width="1166" height="815" fill="none" stroke="var(--marquee-yellow)" stroke-width="12" stroke-linecap="round" stroke-dasharray="0 21.5"/>
  </svg>

  <div class="club-mark">LVH</div>

  <p class="presenter">Lakeview Veterans Hall Poker Club presents</p>
  <h1 class="event-title">ANNUAL $200 BUY IN TOURNAMENT</h1>
  <p class="event-date weekend">OCTOBER LONG WEEK END</p>
  <p class="event-date days">4-5 OCTOBER 2014</p>

  <svg class="stack-burst" viewBox="0 0 200 200" aria-hidden="true">
    <defs>
      <linearGradient id="burstFill" x1="0" y1="0" x2="0" y2="1">
        <stop offset="0" stop-color="var(--burst-top)"/>
        <stop offset="1" stop-color="var(--burst-bottom)"/>
      </linearGradient>
    </defs>
    <polygon fill="url(#burstFill)" points="100,0 113,32 140,8 139,44 174,30 160,62 198,64 168,88 200,108 164,120 184,152 146,148 150,186 120,164 100,198 80,164 50,186 54,148 16,152 36,120 0,108 32,88 2,64 40,62 26,30 61,44 60,8 87,32"/>
  </svg>
  <div class="stack-burst-text">
    <p>$100k<br>Starting Stack</p>
    <p class="blinds">45 Min Blinds</p>
  </div>

  <section class="details">
    <p class="label">Venue:</p>
    <p>Lakeview Veterans Hall</p>
    <p>42 Kerridge Lane</p>
    <p>Mount Gambier Sa 5290</p>
    <p class="gap"><span class="label">Time:</span> 10:00am Start (Sa Time)</p>
    <p><span class="label">Registration:</span>&nbsp; 9:30am (Sa Time)</p>
    <p class="gap-wide"><span class="label">Email:</span> lvhcards@mailnest.com.au</p>
  </section>

  <div class="social">
    <span class="social-tag"><span class="dot"></span>Find us on Friendbook</span>
    <span>LVH Cards 2014</span>
  </div>

  <div class="chips-photo" role="img" aria-label="Photo of stacked red poker chips on a dark table"></div>
</main>
</body>
</html>
```